Website Redesign Brief for Breezeline Cooling Services WA

Creating a clear and concise brief for designers to redesign your website, https://breezelinecoolingwa.com.au/, is essential to ensure the project aligns with your vision for a more energetic, friendly, optimistic, and user-friendly website. Below is a sample brief tailored to your request, balancing specificity with flexibility to allow designers to bring their creativity to the table.

Website Redesign Brief for Breezeline Cooling WA
1. Project Overview

We are seeking a redesign of our website, https://breezelinecoolingwa.com.au/, to create a vibrant, engaging, and user-friendly online presence that reflects our brand’s commitment to providing top-notch air conditioning services in Western Australia. The redesigned website should feel energetic, friendly, and optimistic while maintaining professionalism and improving user experience.
2. Goals and Objectives

Enhance Brand Perception: Convey a modern, approachable, and positive brand identity that resonates with both residential and commercial clients.
Improve User Experience: Simplify navigation, improve accessibility, and ensure a seamless experience across devices (desktop, tablet, mobile).
Increase Engagement: Encourage visitors to explore services, request quotes, and contact us through clear calls-to-action (CTAs).
Boost Conversion Rates: Make it easier for users to find information and take action (e.g., booking services or inquiries).
Showcase Expertise: Highlight our professional air conditioning services, experience, and customer satisfaction in an inviting way.

3. Target Audience

Primary Audience: Homeowners and small business owners in Western Australia seeking air conditioning installation, maintenance, or repair services.
Secondary Audience: Property managers, commercial clients, and real estate professionals looking for reliable HVAC solutions.
Demographics: Ages 25–65, mix of tech-savvy and non-tech-savvy users, located primarily in Perth and surrounding areas.
User Needs: Clear information about services, transparent pricing, easy contact options, and reassurance of quality and reliability.

4. Design Preferences

Tone and Style:

Energetic: Use bold, vibrant colors (e.g., blues, whites, and pops of warm tones like orange or yellow) to evoke energy and optimism.
Friendly: Incorporate approachable language, welcoming imagery, and a clean, uncluttered layout.
Optimistic: Highlight positive customer outcomes (e.g., comfort, energy savings) through visuals and messaging.
Professional yet approachable: Maintain credibility as a trusted service provider while avoiding a cold or overly corporate feel.

Visual Elements:

Use high-quality images of happy customers, comfortable homes/offices, and modern air conditioning units.
Incorporate subtle animations or micro-interactions to add energy (e.g., hover effects on buttons or smooth scrolling).
Avoid overly complex graphics that may slow down the site or distract from usability.

Typography: Clean, modern fonts that are easy to read. Use larger, bold headings for hierarchy and warmth.
Inspiration: Websites like https://www.polarvane.com.au/ (clean and professional) or https://www.kestrelthermaltech.com.au/ (user-friendly and modern) but with a more vibrant and welcoming vibe.

5. Functional Requirements

User-Friendly Navigation: Simplify the menu structure to make key pages (e.g., Services, About Us, Contact) easily accessible.
Mobile Responsiveness: Ensure the site is fully optimized for mobile devices, with fast load times and intuitive touch interactions.
Key Features:

Prominent CTAs for requesting quotes, booking services, or contacting the team.
A clear service overview with icons or visuals for each service (e.g., installation, repairs, maintenance).
A testimonials section to showcase customer satisfaction.
An easy-to-use contact form with minimal fields.
Integration with Google Maps for location-based services or office directions.

SEO and Performance: Optimize for search engines (e.g., keywords like “air conditioning Perth”) and ensure fast loading speeds.
Accessibility: Follow WCAG guidelines to ensure the site is usable for all visitors, including those with disabilities.

6. Content Guidance

Existing Content: Review and refine current content from https://breezelinecoolingwa.com.au/ to make it concise, engaging, and aligned with the friendly tone.
New Content Ideas:

Add a “Why Choose Us” section highlighting expertise, customer service, and eco-friendly solutions.
Include a FAQ page to address common customer questions.
Create a blog section for tips on air conditioning maintenance or energy efficiency (optional).

Tone of Voice: Conversational, reassuring, and positive. Avoid technical jargon unless clearly explained.

7. Technical Considerations

Platform: Open to recommendations (e.g., WordPress, Wix, or custom-built) but prioritize ease of maintenance and scalability.
Integrations: Ensure compatibility with existing tools (e.g., Google Analytics, CRM for quote requests, or booking systems).
Domain and Hosting: Retain current domain (breezelinecoolingwa.com.au); hosting recommendations welcome.
Timeline: Initial design concepts within [insert timeline, e.g., 2–3 weeks], with full redesign completed by [insert deadline, e.g., 6–8 weeks].
Budget: [Insert budget range or state “flexible, please provide a quote”].

8. Deliverables

Wireframes and mockups for homepage, service pages, and contact page.
Fully responsive website design with all necessary pages.
Style guide (colors, fonts, imagery guidelines).
CMS setup (if applicable) with basic training for content updates.
Testing and optimization for performance and SEO.

9. Success Metrics

Increased time on site and reduced bounce rate.
Higher conversion rates for quote requests and contact form submissions.
Positive user feedback on ease of navigation and overall experience.
Improved search engine rankings for key terms within [insert timeframe, e.g., 3 months].

10. Additional Notes

Please provide a portfolio of similar projects or examples of user-friendly, vibrant websites.
We are open to creative suggestions to make the website stand out in the HVAC industry.
Regular progress updates and collaboration during the design process are appreciated.
Updates

designers are asking for more time

few have requested an extension. I Have extended

Target Market(s)

Primary Audience: Homeowners and small business owners in Western Australia seeking air conditioning installation, maintenance, or repair services. Secondary Audience: Property managers, commercial clients, and real estate professionals looking for reliable HVAC solutions. Demographics: Ages 25–65, mix of tech-savvy and non-tech-savvy users, located primarily in Perth and surrounding areas. User Needs: Clear information about services, transparent pricing, easy contact options, and reassurance of quality and reliability.

Industry/Entity Type

Air Conditioning and Refrigeration (HVAC & R)

Coding

Coded - Design and coding required

Colors
0054AA
0677BA
7BADD7
CADEEF
E8F1F8
59FF00
82FF00
B8FF75
E3FFCB
F4FFEA
F0912C
F2A743
F7CA91
FBE8D2
FDF5EE
EE7325
F08F49
F5BC92
FAE3D3
FDF4ED

Requirements
Must have
• Must have all my current information I currently have on my web page.
Nice to have
• A sales page for people to buy products online

```html
<!DOCTYPE html>
<html lang="en">
<head>
<meta charset="UTF-8">
<title>Breezeline Cooling Services WA</title>
<link href="https://fonts.googleapis.com/css2?family=Poppins:wght@400;500;600;700&display=swap" rel="stylesheet">
<style>
:root{
  --navy:#1a2f5c;
  --navy-deep:#142548;
  --orange:#ee7325;
  --orange-soft:#fdf4ed;
  --sky:#e8f1f8;
  --mist:#f2f6fb;
  --ink:#1f2a44;
  --grey:#5b6478;
  --line:#dde3ec;
  --white:#ffffff;
}
*{box-sizing:border-box;margin:0;padding:0}
html,body{width:1200px;height:5159px;overflow:hidden}
body{font-family:'Poppins',sans-serif;color:var(--ink);background:var(--white);position:relative}
.section{position:absolute;left:0;width:1200px}
.abs{position:absolute}
.photo{position:absolute}
.btn{position:absolute;background:var(--orange);color:#fff;font-weight:600;font-size:13px;border-radius:22px;display:flex;align-items:center;justify-content:center;text-transform:uppercase;letter-spacing:.3px}
.heading{position:absolute;left:0;width:1200px;text-align:center;font-weight:600;font-size:30px;color:var(--navy);letter-spacing:.5px}
.brand-name{font-weight:600;color:var(--navy);font-size:12px;line-height:1.2}
/* header */
.site-header{top:0;height:90px;z-index:5}
.logo{left:60px;top:18px;display:flex;align-items:center;gap:8px;width:130px}
.logo .dot{width:22px;height:22px;border-radius:50%;background:var(--orange);flex:none}
.nav{left:298px;top:36px;display:flex;gap:0;font-size:12.5px}
.nav a{color:var(--ink);text-decoration:none;margin-right:0}
.nav a.active{color:var(--orange)}
.nav-items{position:absolute;left:0;top:0;width:640px;height:20px}
.nav-items a{position:absolute;top:0}
.call-pill{left:962px;top:24px;width:178px;height:40px;border-radius:22px;background:var(--orange);color:#fff;font-weight:600;font-size:14px;display:flex;align-items:center;justify-content:center;gap:8px}
/* hero */
.hero{top:0;height:700px;overflow:hidden}
.hero-photo{left:0;top:0;width:1200px;height:700px;background:linear-gradient(100deg,#f7f7f5 0%,#f1efea 40%,#d9c8b4 62%,#c9a98a 78%,#e8e2da 100%)}
.hero-title{left:60px;top:222px;font-size:41px;font-weight:600;line-height:1.28;color:var(--navy)}
.hero-text{left:62px;top:345px;width:490px;font-size:14px;line-height:1.75;color:var(--ink)}
.hero .btn{left:60px;top:443px;width:172px;height:40px}
/* services */
.services{top:740px;height:500px}
.services .heading{top:28px}
.service-card{position:absolute;top:100px;width:292px;height:305px;border-radius:14px;background:var(--mist)}
.service-card.warm{background:var(--orange-soft)}
.service-card .photo{left:16px;top:16px;width:260px;height:184px;border-radius:12px}
.service-card .arrow{position:absolute;left:122px;top:177px;width:48px;height:48px;border-radius:50%;background:var(--navy);display:flex;align-items:center;justify-content:center}
.service-card.warm .arrow{background:var(--orange)}
.service-card h3{position:absolute;top:246px;left:0;width:100%;text-align:center;font-size:15px;font-weight:500}
.services .btn{left:506px;top:448px;width:188px;height:40px}
/* air con */
.aircon{top:1295px;height:550px;overflow:hidden;background:var(--mist)}
.aircon-photo{left:0;top:0;width:640px;height:550px;background:linear-gradient(120deg,#8a5a3c 0%,#a9765a 30%,#cfd6df 55%,#eef1f5 100%)}
.aircon h2{left:645px;top:112px;font-size:29px;font-weight:600;color:var(--navy)}
.aircon p{left:645px;top:160px;width:425px;font-size:12px;line-height:1.9;color:var(--grey)}
.video-thumb{left:644px;top:293px;width:134px;height:80px;border-radius:8px;background:linear-gradient(135deg,#6b7585,#b9c1cc)}
.video-thumb .play{position:absolute;left:54px;top:27px;width:26px;height:26px;border-radius:50%;background:#fff;display:flex;align-items:center;justify-content:center}
.call-block{left:800px;top:313px;display:flex;align-items:center;gap:14px}
.call-icon{width:36px;height:36px;border-radius:50%;background:var(--orange);display:flex;align-items:center;justify-content:center}
.call-block small{display:block;font-size:11px;color:var(--ink)}
.call-block strong{display:block;font-size:16px;font-weight:600;color:var(--ink)}
.aircon .btn{left:644px;top:402px;width:136px;height:38px}
/* why */
.why{top:1900px;height:520px}
.why .heading{top:20px}
.logo-pill{left:455px;top:92px;width:290px;height:120px;border:3px solid var(--navy);border-radius:60px;display:flex;align-items:center;justify-content:center}
.logo-pill .inner{width:262px;height:94px;border:3px solid var(--orange);border-radius:48px;display:flex;align-items:center;justify-content:center;gap:8px}
.why-card{position:absolute;top:300px;width:204px;height:205px;border-radius:6px;background:var(--navy);color:#fff;padding:28px 24px}
.why-card.orange{background:var(--orange)}
.why-card h3{font-size:15px;font-weight:600;margin-top:18px;line-height:1.3}
.why-card p{font-size:11.5px;line-height:1.7;margin-top:10px;opacity:.95}
/* faq */
.faq{top:2475px;height:610px;overflow:hidden;background:var(--mist)}
.faq-photo{left:540px;top:0;width:660px;height:610px;background:linear-gradient(110deg,#e9edf2 0%,#d6dbe2 45%,#c5cbd3 100%)}
.faq h2{left:62px;top:110px;font-size:29px;font-weight:600;color:var(--navy)}
.faq-item{position:absolute;left:60px;width:465px;background:#fff;border:1px solid var(--line);border-radius:4px;padding:0 20px;font-size:14px}
.faq-item .q{height:48px;display:flex;align-items:center;justify-content:space-between}
.faq-item .a{font-size:11.5px;color:var(--grey);line-height:1.6;margin-top:-4px}
/* testimonial */
.testimonial{top:3100px;height:440px}
.testimonial .heading{top:60px}
.avatar{position:absolute;border-radius:50%;background:linear-gradient(135deg,#c89b7b,#7a5a48)}
.testimonial blockquote{left:476px;top:186px;width:392px;font-size:12.5px;line-height:1.65;color:var(--grey)}
.testimonial cite{left:476px;top:295px;font-size:10.5px;color:var(--grey);font-style:normal}
.slider-line{left:476px;top:339px;width:400px;height:1px;background:var(--line)}
.slider-btn{position:absolute;top:324px;width:32px;height:32px;border-radius:50%;display:flex;align-items:center;justify-content:center}
/* brands */
.brands{top:3545px;height:370px;overflow:hidden}
.brands .heading{top:132px}
.brand-logo{position:absolute;top:210px;height:40px;display:flex;align-items:center;gap:8px;font-weight:600;font-size:20px;color:var(--navy)}
.brand-logo .mark{width:18px;height:18px;border-radius:50%;background:var(--navy)}
/* blogs */
.blogs{top:3955px;height:380px}
.blogs .heading{top:20px}
.blog-card{position:absolute;top:100px;width:350px;height:246px;border-radius:6px;background:var(--mist);overflow:hidden}
.blog-card.warm{background:var(--orange-soft)}
.blog-card .photo{left:0;top:0;width:350px;height:172px}
.blog-card h3{position:absolute;left:24px;top:188px;width:230px;font-size:14px;font-weight:600;line-height:1.55}
/* contact */
.contact{top:4375px;height:480px;overflow:hidden;background:var(--mist)}
.contact-photo{left:170px;top:40px;width:420px;height:420px;background:radial-gradient(ellipse at 45% 40%,#2a3b63 0%,#4a5a7e 45%,rgba(238,243,249,0) 72%)}
.contact h2{left:630px;top:90px;font-size:29px;font-weight:600;color:var(--navy)}
.field{position:absolute;background:#fff;border:1px solid var(--line);border-radius:4px;font-size:11.5px;color:var(--grey);padding:10px 12px}
.field.active{border-color:#9aa3b3}
.contact .btn{left:632px;top:362px;width:126px;height:38px}
/* footer */
.footer{top:4855px;height:304px}
.footer .logo-f{left:60px;top:50px;display:flex;align-items:center;gap:8px;width:140px}
.footer .about{left:60px;top:136px;width:250px;font-size:12px;line-height:1.6;color:var(--grey)}
.social{position:absolute;top:196px;width:32px;height:32px;border-radius:50%;background:var(--orange)}
.footer h4{font-size:17px;font-weight:600;color:var(--orange)}
.foot-nav{left:426px;top:44px}
.foot-nav ul{list-style:none;margin-top:12px}
.foot-nav li{font-size:12px;color:var(--grey);line-height:22.5px}
.foot-contact{left:790px;top:44px}
.contact-row{position:absolute;left:0;display:flex;align-items:flex-start;gap:16px;font-size:12px;color:var(--grey);width:300px}
.contact-row .ic{width:32px;height:32px;border-radius:50%;background:var(--orange);display:flex;align-items:center;justify-content:center;flex:none}
.copyright{left:60px;top:268px;width:1080px;border-top:1px solid var(--line);padding-top:12px;text-align:center;font-size:11.5px;color:var(--ink)}
</style>
</head>
<body>

<!-- Hero -->
<section class="section hero">
  <div class="photo hero-photo" role="img" aria-label="Smiling mother lifting her young daughter in a bright living room beneath a split-system air conditioner"></div>
  <svg class="abs" style="left:0;top:0" width="1200" height="700" viewBox="0 0 1200 700" aria-hidden="true">
    <path d="M0 500 Q560 700 1200 600 L1200 700 L0 700Z" fill="#1a2f5c"/>
    <path d="M0 655 Q620 730 1200 612 L1200 700 L0 700Z" fill="#ffffff"/>
  </svg>
  <h1 class="abs hero-title">QUALITY AIR<br>CONDITIONING SERVICES</h1>
  <p class="abs hero-text">Our service is second to none; we have a team of experienced technicians that consistently deliver the best quality air conditioner repairs Perth has to offer.</p>
  <a class="btn">Book a Services</a>
</section>

<!-- Header -->
<header class="section site-header">
  <div class="abs logo"><span class="dot"></span><span class="brand-name">Breezeline Cooling Services WA</span></div>
  <nav class="abs nav">
    <div class="nav-items">
      <a class="active" style="left:0">Home</a>
      <a style="left:86px">About Us</a>
      <a style="left:192px">Services</a>
      <a style="left:290px">Why Choose Us</a>
      <a style="left:437px">FAQ</a>
      <a style="left:506px">Blog</a>
      <a style="left:581px">Contact</a>
    </div>
  </nav>
  <div class="abs call-pill">
    <svg width="14" height="14" viewBox="0 0 24 24" fill="#fff" aria-hidden="true"><path d="M6.6 10.8a15.1 15.1 0 0 0 6.6 6.6l2.2-2.2c.3-.3.7-.4 1-.2 1.1.4 2.3.6 3.6.6.6 0 1 .4 1 1V20c0 .6-.4 1-1 1C10.6 21 3 13.4 3 4c0-.6.4-1 1-1h3.5c.6 0 1 .4 1 1 0 1.3.2 2.5.6 3.6.1.3 0 .7-.2 1z"/></svg>
    + 0400 555 218
  </div>
</header>

<!-- Services -->
<section class="section services">
  <h2 class="heading">OUR SERVICES</h2>
  <article class="service-card" style="left:150px">
    <div class="photo" role="img" aria-label="Technician in hard hat installing commercial rooftop condenser units" style="background:linear-gradient(135deg,#8fa3b8,#d0702f 70%,#5a6c80)"></div>
    <span class="arrow"><svg width="18" height="18" viewBox="0 0 24 24" fill="none" stroke="#fff" stroke-width="2.4"><path d="M4 12h15M13 6l6 6-6 6"/></svg></span>
    <h3>Commercial Installation</h3>
  </article>
  <article class="service-card warm" style="left:454px">
    <div class="photo" role="img" aria-label="Technician servicing an indoor split-system unit with a screwdriver" style="background:linear-gradient(135deg,#e9ecef,#b7bec7 60%,#6e7681)"></div>
    <span class="arrow"><svg width="18" height="18" viewBox="0 0 24 24" fill="none" stroke="#fff" stroke-width="2.4"><path d="M4 12h15M13 6l6 6-6 6"/></svg></span>
    <h3>Domestic Installation</h3>
  </article>
  <article class="service-card" style="left:758px">
    <div class="photo" role="img" aria-label="Interior of a cool room lined with stocked metal shelving" style="background:linear-gradient(90deg,#6f7680,#d8dce1 50%,#6f7680)"></div>
    <span class="arrow"><svg width="18" height="18" viewBox="0 0 24 24" fill="none" stroke="#fff" stroke-width="2.4"><path d="M4 12h15M13 6l6 6-6 6"/></svg></span>
    <h3>Coolroom Installation</h3>
  </article>
  <a class="btn">View All Services</a>
</section>

<!-- Air conditioning -->
<section class="section aircon">
  <div class="photo aircon-photo" role="img" aria-label="Smiling technician mounting an outdoor air conditioning unit on a wall"></div>
  <svg class="abs" style="left:0;top:0" width="1200" height="550" viewBox="0 0 1200 550" aria-hidden="true">
    <path d="M0 0 L1200 0 L1200 40 Q900 0 640 20 Q300 50 0 60Z" fill="#ffffff"/>
    <path d="M680 20 Q1000 10 1200 40 L1200 160 Q1100 40 680 20Z" fill="#1a2f5c"/>
    <path d="M0 330 Q120 480 560 520 L0 520Z" fill="#1a2f5c"/>
    <path d="M0 550 L0 505 Q600 560 1200 440 L1200 550Z" fill="#ffffff"/>
  </svg>
  <h2 class="abs">AIR CONDITIONING</h2>
  <p class="abs">Our service is second to none; our team of experienced technicians that consistently deliver the best quality air conditioner repairs Perth has to offer. There are many different brands of air conditioning on the market, each with their own way of controlling the temperature of your home.</p>
  <div class="abs video-thumb" role="img" aria-label="Video preview of a technician at work"><span class="play"><svg width="10" height="10" viewBox="0 0 10 10"><path d="M2 1l7 4-7 4z" fill="#ee7325"/></svg></span></div>
  <div class="abs call-block">
    <span class="call-icon"><svg width="16" height="16" viewBox="0 0 24 24" fill="#fff"><path d="M6.6 10.8a15.1 15.1 0 0 0 6.6 6.6l2.2-2.2c.3-.3.7-.4 1-.2 1.1.4 2.3.6 3.6.6.6 0 1 .4 1 1V20c0 .6-.4 1-1 1C10.6 21 3 13.4 3 4c0-.6.4-1 1-1h3.5c.6 0 1 .4 1 1 0 1.3.2 2.5.6 3.6.1.3 0 .7-.2 1z"/></svg></span>
    <div><small>Call to Action</small><strong>+ 0400 555 218</strong></div>
  </div>
  <a class="btn">View More</a>
</section>

<!-- Why choose us -->
<section class="section why">
  <h2 class="heading">WHY CHOOES US</h2>
  <div class="abs logo-pill"><div class="inner"><span class="logo dot" style="width:18px;height:18px;border-radius:50%;background:#ee7325;display:block"></span><span class="brand-name" style="font-size:12px">Breezeline Cooling Services WA</span></div></div>
  <svg class="abs" style="left:370px;top:210px" width="460" height="90" viewBox="0 0 460 90" fill="none" aria-hidden="true">
    <path d="M205 2 V20 Q205 30 195 30 H22 Q10 30 10 42 V72" stroke="#1a2f5c" stroke-width="2.5"/>
    <path d="M255 2 V20 Q255 30 265 30 H438 Q450 30 450 42 V72" stroke="#1a2f5c" stroke-width="2.5"/>
    <path d="M230 2 V72" stroke="#ee7325" stroke-width="2.5"/>
    <circle cx="205" cy="4" r="4" fill="#1a2f5c"/><circle cx="255" cy="4" r="4" fill="#1a2f5c"/><circle cx="230" cy="4" r="4" fill="#ee7325"/>
    <circle cx="10" cy="75" r="4" fill="#1a2f5c"/><circle cx="450" cy="75" r="4" fill="#1a2f5c"/><circle cx="230" cy="75" r="4" fill="#ee7325"/>
  </svg>
  <article class="why-card" style="left:278px">
    <svg width="44" height="44" viewBox="0 0 44 44" fill="none" stroke="#fff" stroke-width="1.6"><circle cx="22" cy="26" r="10"/><circle cx="22" cy="26" r="4"/><path d="M22 4l1.5 3 3 .4-2.2 2 .6 3-2.9-1.5-2.9 1.5.6-3-2.2-2 3-.4z"/><path d="M8 10l1 2 2 .3-1.5 1.4.4 2L8 14.7 6.1 15.7l.4-2L5 12.3l2-.3z"/><path d="M36 10l1 2 2 .3-1.5 1.4.4 2-1.9-1-1.9 1 .4-2-1.5-1.4 2-.3z"/></svg>
    <h3>Expertise</h3>
    <p>Lorem Ipsum has been the industry's standard dummy.</p>
  </article>
  <article class="why-card orange" style="left:497px">
    <svg width="44" height="44" viewBox="0 0 44 44" fill="none" stroke="#fff" stroke-width="1.6"><circle cx="22" cy="20" r="14"/><circle cx="22" cy="17" r="5"/><path d="M13 30c2-5 16-5 18 0"/><path d="M12 36l-4 4M32 36l4 4"/></svg>
    <h3>Customer Service</h3>
    <p>Lorem Ipsum has been the industry's standard dummy.</p>
  </article>
  <article class="why-card" style="left:716px">
    <svg width="44" height="44" viewBox="0 0 44 44" fill="none" stroke="#fff" stroke-width="1.6"><circle cx="22" cy="22" r="10"/><path d="M22 28c-4-3-4-8 0-12 4 4 4 9 0 12zM22 28v6"/><path d="M22 4v5M22 35v5M4 22h5M35 22h5M9 9l3.5 3.5M31.5 31.5L35 35M35 9l-3.5 3.5M12.5 31.5L9 35"/></svg>
    <h3>Eco-friendly Solutions</h3>
    <p>Lorem Ipsum has been the industry's.</p>
  </article>
</section>

<!-- FAQ -->
<section class="section faq">
  <div class="photo faq-photo" role="img" aria-label="Technician in a grey uniform showing a tablet to a smiling customer"></div>
  <svg class="abs" style="left:0;top:0" width="1200" height="610" viewBox="0 0 1200 610" aria-hidden="true">
    <path d="M0 0 H1200 V20 Q900 -10 520 10 Q220 30 0 40Z" fill="#ffffff"/>
    <path d="M620 10 Q980 0 1200 20 V190 Q1080 20 620 10Z" fill="#1a2f5c"/>
    <path d="M0 380 Q120 540 620 600 L0 600Z" fill="#1a2f5c"/>
    <path d="M0 610 V590 Q700 640 1200 520 V610Z" fill="#ffffff"/>
  </svg>
  <h2 class="abs">FAQ'S</h2>
  <div class="faq-item" style="top:175px"><div class="q"><span>dummy text ever since the 1500s ?</span><svg width="12" height="8" viewBox="0 0 12 8" fill="none" stroke="#1f2a44" stroke-width="1.6"><path d="M1 7l5-5 5 5"/></svg></div></div>
  <div class="faq-item" style="top:238px;height:108px"><div class="q"><span>Lorem Ipsum has been the industry's ?</span><svg width="12" height="8" viewBox="0 0 12 8" fill="none" stroke="#1f2a44" stroke-width="1.6"><path d="M1 1l5 5 5-5"/></svg></div><p class="a">Lorem Ipsum has been the industry's standard dummy<br>text ever since the 1500s</p></div>
  <div class="faq-item" style="top:358px"><div class="q"><span>when an unknown printer took a galley ?</span><svg width="12" height="8" viewBox="0 0 12 8" fill="none" stroke="#1f2a44" stroke-width="1.6"><path d="M1 7l5-5 5 5"/></svg></div></div>
</section>

<!-- Testimonial -->
<section class="section testimonial">
  <h2 class="heading">TESTIMONIAL</h2>
  <svg class="abs" style="left:260px;top:140px" width="140" height="240" viewBox="0 0 140 240" fill="none" aria-hidden="true"><path d="M110 10 Q0 50 10 130 Q20 200 110 230" stroke="#d5dbe4" stroke-width="1.5"/></svg>
  <div class="avatar" role="img" aria-label="Customer portrait" style="left:348px;top:136px;width:56px;height:56px;background:linear-gradient(135deg,#7da0c4,#3a5274)"></div>
  <div class="avatar" role="img" aria-label="Customer portrait" style="left:232px;top:252px;width:56px;height:56px"></div>
  <div class="avatar" role="img" aria-label="Featured customer portrait" style="left:320px;top:230px;width:108px;height:108px;background:linear-gradient(135deg,#d3c6b6,#7b5b47)"></div>
  <div class="avatar" role="img" aria-label="Customer portrait" style="left:344px;top:358px;width:60px;height:60px;background:linear-gradient(135deg,#c9a07f,#4b3428)"></div>
  <blockquote class="abs">Lorem Ipsum has been the industry's standard dummy text ever since the 1500s, when an unknown printer took a galley of type and scrambled it to make a type specimen book. It has survived not only five centuries, but also the leap into electronic typesetting.</blockquote>
  <cite class="abs">Lorem Ipsum has been the industry's standard.</cite>
  <div class="abs slider-line"></div>
  <span class="slider-btn" style="left:880px;background:#ee7325"><svg width="10" height="12" viewBox="0 0 10 12" fill="none" stroke="#fff" stroke-width="1.8"><path d="M7 1L2 6l5 5"/></svg></span>
  <span class="slider-btn" style="left:920px;background:#fff;border:1px solid #1a2f5c"><svg width="10" height="12" viewBox="0 0 10 12" fill="none" stroke="#1a2f5c" stroke-width="1.8"><path d="M3 1l5 5-5 5"/></svg></span>
</section>

<!-- Brands -->
<section class="section brands">
  <svg class="abs" style="left:0;top:0" width="1200" height="370" viewBox="0 0 1200 370" aria-hidden="true">
    <path d="M0 70 Q600 0 1200 40 V330 Q600 400 0 340Z" fill="#f2f6fb"/>
    <path d="M640 10 Q1000 0 1200 40 V130 Q1080 20 640 10Z" fill="#1a2f5c"/>
    <path d="M0 170 Q60 330 520 360 L0 360Z" fill="#1a2f5c"/>
    <path d="M0 370 V355 Q600 385 1200 320 V370Z" fill="#ffffff"/>
  </svg>
  <h2 class="heading">OUR RECOMMENDED BRANDS</h2>
  <div class="brand-logo" style="left:200px"><span>Northgale</span><span class="mark"></span></div>
  <div class="brand-logo" style="left:420px"><span>Polarvane</span></div>
  <div class="brand-logo" style="left:655px"><span class="mark"></span><span>Ventora</span></div>
  <div class="brand-logo" style="left:870px;font-size:17px"><span class="mark" style="border-radius:0"></span><span>Kestrel Thermaltech</span></div>
</section>

<!-- Blogs -->
<section class="section blogs">
  <h2 class="heading">LATEST BLOGS</h2>
  <article class="blog-card" style="left:60px">
    <div class="photo" role="img" aria-label="Technician cleaning the filter of a wall-mounted air conditioner" style="background:linear-gradient(135deg,#eef0f2,#aeb5bd 60%,#5c6570)"></div>
    <h3>Lorem Ipsum has been the industry's</h3>
  </article>
  <article class="blog-card warm" style="left:425px">
    <div class="photo" role="img" aria-label="Technician in a hi-vis vest checking refrigerant gauges on a rooftop unit" style="background:linear-gradient(135deg,#b55c40,#d7c27a 50%,#6f7a86)"></div>
    <h3>Lorem Ipsum has been the industry's</h3>
  </article>
  <article class="blog-card" style="left:790px">
    <div class="photo" role="img" aria-label="Technician installing ducting in a ceiling" style="background:linear-gradient(135deg,#f1f2f4,#c4c9cf 55%,#7a828c)"></div>
    <h3>Lorem Ipsum has been the industry's</h3>
  </article>
</section>

<!-- Contact -->
<section class="section contact">
  <svg class="abs" style="left:0;top:0" width="1200" height="480" viewBox="0 0 1200 480" aria-hidden="true">
    <path d="M0 0 H1200 V40 Q700 -10 0 60Z" fill="#ffffff"/>
    <path d="M560 20 Q1000 0 1200 40 V120 Q1050 20 560 20Z" fill="#1a2f5c"/>
    <path d="M0 260 Q80 440 600 470 L0 470Z" fill="#1a2f5c"/>
    <path d="M0 480 V468 Q700 500 1200 400 V480Z" fill="#ffffff"/>
  </svg>
  <div class="photo contact-photo" role="img" aria-label="Smiling technician in navy overalls holding a red toolbox"></div>
  <h2 class="abs">GET IN TOUCH</h2>
  <div class="field active" style="left:630px;top:146px;width:188px;height:40px">First name *</div>
  <div class="field" style="left:828px;top:146px;width:188px;height:40px">Last name *</div>
  <div class="field" style="left:630px;top:198px;width:188px;height:40px">Email *</div>
  <div class="field" style="left:828px;top:198px;width:188px;height:40px">Phone no *</div>
  <div class="field" style="left:630px;top:250px;width:386px;height:90px">Message *</div>
  <a class="btn">Submit</a>
</section>

<!-- Footer -->
<footer class="section footer">
  <div class="abs logo-f"><span class="logo dot" style="width:22px;height:22px;border-radius:50%;background:#ee7325;display:block;flex:none"></span><span class="brand-name">Breezeline Cooling Services WA</span></div>
  <p class="abs about">Lorem ipsum has been the industry's standard dummy text eve</p>
  <span class="social" role="img" aria-label="Social profile" style="left:60px"></span>
  <span class="social" role="img" aria-label="Social profile" style="left:104px"></span>
  <span class="social" role="img" aria-label="Social profile" style="left:148px"></span>
  <div class="abs foot-nav">
    <h4>Navigation</h4>
    <ul><li>Home</li><li>About</li><li>Service</li><li>Why chooes us</li><li>Faqs</li><li>Blogs</li><li>Contact</li></ul>
  </div>
  <div class="abs foot-contact">
    <h4>Contact</h4>
    <div class="contact-row" style="top:44px"><span class="ic"><svg width="14" height="14" viewBox="0 0 24 24" fill="#fff"><path d="M6.6 10.8a15.1 15.1 0 0 0 6.6 6.6l2.2-2.2c.3-.3.7-.4 1-.2 1.1.4 2.3.6 3.6.6.6 0 1 .4 1 1V20c0 .6-.4 1-1 1C10.6 21 3 13.4 3 4c0-.6.4-1 1-1h3.5c.6 0 1 .4 1 1 0 1.3.2 2.5.6 3.6.1.3 0 .7-.2 1z"/></svg></span><span style="padding-top:7px">+ 0400 555 218</span></div>
    <div class="contact-row" style="top:98px"><span class="ic"><svg width="14" height="12" viewBox="0 0 14 12" fill="none" stroke="#fff" stroke-width="1.5"><rect x="1" y="1" width="12" height="10" rx="1"/><path d="M1 2l6 5 6-5"/></svg></span><span style="padding-top:7px">hello@breezelinecoolingwa.com.au</span></div>
    <div class="contact-row" style="top:152px"><span class="ic"><svg width="12" height="15" viewBox="0 0 12 15" fill="#fff"><path d="M6 0a6 6 0 0 0-6 6c0 4.5 6 9 6 9s6-4.5 6-9a6 6 0 0 0-6-6zm0 8.2A2.2 2.2 0 1 1 6 3.8a2.2 2.2 0 0 1 0 4.4z"/></svg></span><span style="padding-top:2px;line-height:1.6">42 Harbour Lane, Coastview WA<br>6000</span></div>
  </div>
  <p class="abs copyright">Copyright © 2025 Breezeline Cooling. All Rights Reserved.</p>
</footer>

</body>
</html>
```